Conference program advertisement

Our business www.clinicledger.com.au is a good sponsor of the conference program run by the Southern Pacific Guild of Perioperative Physicians (SPGPP) here in Western Australia.
We have been running the same ad for a while and so we could do with a fresh new presence.
We have a conference banner and other signage that we'll use at the trade show so we're not looking to rebrand. Just looking for a new ad.
Specification is full colour A4, high res PDF
(Because I'm using my phone to create this job, I cannot seem to upload the existing ad. I'll do do ASAP.)

Target Market(s)

Specialist doctors

Industry/Entity Type

Trade

Font styles to use
Sans Serif

Colors

Designer to choose colors to be used in the design.

Requirements
Must have
• A4
Existing logo and colour scheme

```html
<!DOCTYPE html>
<html lang="en">
<head>
<meta charset="utf-8">
<title>Clinic Ledger Services – Conference Advertisement</title>
<link href="https://fonts.googleapis.com/css2?family=Pathway+Gothic+One&family=Roboto+Condensed:wght@300;400;700&family=Roboto:wght@400&family=Oswald:wght@400&display=swap" rel="stylesheet">
<style>
  :root {
    --stage: #000000;
    --paper: #ffffff;
    --brand-red: #c01f2f;
    --ink: #1e1e1e;
    --ink-soft: #3a3a3a;
    --band-grey: #d3d4d6;
    --divider: #ffffff;
    --accent-blue: #8ea4cf;
    --photo-light: #eef4fa;
    --photo-mid: #9fc6e6;
    --photo-deep: #5b9fd6;
  }
  * { margin: 0; padding: 0; box-sizing: border-box; }
  html, body { width: 1000px; height: 1200px; overflow: hidden; background: var(--stage); }
  .canvas { position: relative; width: 1000px; height: 1200px; }
  .page { position: absolute; left: 155px; top: 114px; width: 688px; height: 972px; background: var(--paper); overflow: hidden; }

  .portrait { position: absolute; left: 345px; top: 140px; width: 343px; height: 542px; z-index: 1;
    background: radial-gradient(ellipse at 65% 70%, var(--photo-deep) 0%, var(--photo-mid) 40%, var(--photo-light) 72%, var(--paper) 100%);
    clip-path: polygon(70px 0, 100% 0, 100% 100%, 0 100%, 0 380px, 70px 380px); }

  .headline-block { position: absolute; left: 0; top: 0; width: 385px; height: 398px; background: var(--brand-red); border-bottom-right-radius: 56px; z-index: 2; }
  .headline { position: absolute; right: 30px; top: 170px; text-align: right; white-space: nowrap; font-family: "Pathway Gothic One", sans-serif; font-weight: 400; font-size: 60px; line-height: 49px; color: var(--paper); text-transform: uppercase; }
  .headline-mark { position: absolute; left: 390px; top: 268px; z-index: 3; font-family: "Oswald", sans-serif; font-size: 88px; line-height: 1; color: var(--brand-red); }

  .intro { position: absolute; left: 70px; top: 441px; z-index: 2; white-space: nowrap; font-family: "Roboto Condensed", sans-serif; font-weight: 300; font-size: 13.2px; line-height: 20.2px; color: var(--ink); }
  .quote-bracket { position: absolute; width: 26px; height: 14px; z-index: 2; }
  .quote-bracket.open { left: 55px; top: 429px; border-left: 3px solid var(--accent-blue); border-top: 3px solid var(--accent-blue); border-top-left-radius: 6px; }
  .quote-bracket.close { left: 211px; top: 652px; border-right: 3px solid var(--accent-blue); border-bottom: 3px solid var(--accent-blue); border-bottom-right-radius: 6px; }

  .services { position: absolute; left: 0; top: 692px; width: 688px; height: 142px; background: var(--band-grey); }
  .service-column { position: absolute; top: 14px; list-style: none; white-space: nowrap; font-family: "Roboto", sans-serif; font-size: 12px; line-height: 15px; text-transform: uppercase; color: var(--ink); }
  .service-column li { margin-bottom: 8.5px; }
  .service-column li.is-accent { color: var(--brand-red); }
  .service-column.col-a { left: 70px; }
  .service-column.col-b { left: 250px; }
  .service-column.col-c { left: 460px; }
  .column-rule { position: absolute; top: 14px; width: 1px; height: 118px; background: var(--divider); }
  .column-rule.r1 { left: 223px; }
  .column-rule.r2 { left: 433px; }

  .contact { position: absolute; left: 70px; top: 883px; font-style: normal; white-space: nowrap; font-family: "Roboto Condensed", sans-serif; font-weight: 400; font-size: 11px; line-height: 17px; color: var(--ink-soft); }
  .contact strong { color: var(--ink); font-weight: 700; }

  .brand { position: absolute; left: 449px; top: 874px; display: flex; align-items: center; gap: 12px; }
  .brand-square { width: 66px; height: 66px; background: var(--band-grey); }
  .brand-name { font-family: "Roboto", sans-serif; font-weight: 400; font-size: 16.5px; line-height: 16px; color: var(--brand-red); text-transform: uppercase; }
</style>
</head>
<body>
<div class="canvas">
  <article class="page">
    <div class="portrait" role="img" aria-label="Photo of a smiling doctor in blue scrubs with a stethoscope, holding a clipboard"></div>

    <div class="headline-block">
      <h1 class="headline">Is administration<br>eating up<br>your<br>valuable time</h1>
    </div>
    <span class="headline-mark">?</span>

    <span class="quote-bracket open"></span>
    <p class="intro">Admin can consume a large amount of time for<br>doctors working in private practice. From generating<br>accounts to chasing up bad debts, from sitting on<br>hold with health funds, or trawling through<br>remittance advices to getting accreditation papers<br>and submitting provider number applications<br>properly – we’re sure you would prefer to focus on<br>being a doctor rather than worrying about paperwork<br>and piles of admin. Clinic Ledger Services is<br>here to help – contact us today if you’re ready to<br>remove the burden of admin.</p>
    <span class="quote-bracket close"></span>

    <section class="services">
      <ul class="service-column col-a">
        <li>Private billing</li>
        <li class="is-accent">VMP billing</li>
        <li>Practice management</li>
        <li class="is-accent">Organise lists</li>
        <li>Cover lists</li>
      </ul>
      <span class="column-rule r1"></span>
      <ul class="service-column col-b">
        <li class="is-accent">Banking</li>
        <li>Medibenefit and health fund<br>registrations</li>
        <li class="is-accent">Fee estimates and<br>informed<br>financial consent</li>
      </ul>
      <span class="column-rule r2"></span>
      <ul class="service-column col-c">
        <li>Direct Bill and credit card<br>payments</li>
        <li class="is-accent">Electronic claiming to<br>health funds</li>
        <li>GST reporting</li>
        <li class="is-accent">Hospital accreditations</li>
      </ul>
    </section>

    <address class="contact">
      <strong>Sam Whitford</strong> Mobile +61 400 555 182 &nbsp;|&nbsp; Office 08 6100 4417 • Fax 08 6100 4418<br>
      Level 2, Suite 12, 450 Harbour Road, PO Box 318, East Perth WA 6004<br>
      sam@clinicledger.com.au &nbsp;|&nbsp; www.clinicledger.com.au
    </address>

    <div class="brand">
      <span class="brand-square"></span>
      <span class="brand-name">Clinic<br>Ledger<br>Services</span>
    </div>
  </article>
</div>
</body>
</html>
```